Energy Management - layout ideas in Photoshop + $20 participation to 2nd & 3rd place

Dear Designers

• I am looking for an Graphic designer with web experience
• No Html or CSS coding will be required

$20 participation payments to second & third place designs !

This project is for a design theme we can use for our new web site @

http://www.brightgridlink.co.uk/

Basically we like the homepage designs & "Providing the Results" slogan but I'm not quite happy using a template and require slight changes to make it look more bespoke & original .

I only require illustrations if you can come up with the layout as Photoshop, Vector, power point or similar formats we can use them when coding the site .
Inspiration & Similar web sites

http://www.vorandix.com/
http://www.palvora.com/
http://www.dtrgauging.com/
http://www.kelvoran-services.com/
http://www.jx7gaugeportal.co.uk/
http://www.plain-supplyco.com/energy/
http://www.brivowatt.com/solutions/overview
http://www.pqtgb.com/open-system-solutions/

Our other business http://www.dalbygauges.com/remote-meter-reading.html

we have many domains on our dedicated server and will require future help with designs & have more work for the right designer's

here are some examples of clients using our hosted service listed below

http://www.finchpower-monitor.co.uk/

http://www.basaltvolt-monitor.co.uk/

http://www.kpoh-monitor.co.uk/

http://www.keenflow-monitor.co.uk/

http://www.dov-energy.com/

Reason: We have extended the design deadline due to lack of submissions

Reason: We have been unable to give this project our full attention until now Apologies Derek

Target Market(s)

People / Business's who are interested in very advanced Energy related products , saving money and reducing carbon emissions

Industry/Entity Type

Business

Requirements
Must have
• - Clean-professional look

"Providing the Results" slogan

Modern theme based around technology & wireless networking

must be based around the http://www.brightgridlink.co.uk/ theme concept
Nice to have
• Would be nice to point out our Carbon Neutral web site and hosted services

```html
<!DOCTYPE html>
<html lang="en">
<head>
<meta charset="utf-8">
<title>Bright Grid Link – Home</title>
<link href="https://fonts.googleapis.com/css2?family=Arimo:wght@400;700&family=Montserrat:wght@700;800&display=swap" rel="stylesheet">
<style>
:root{
  --sky-edge:#bfe4f8;
  --sky-mid:#e6f5fd;
  --page:#ffffff;
  --ink:#1b1b1b;
  --body:#2a2a2a;
  --rule:#cfcfcf;
  --brand:#1f3f8f;
  --brand-bright:#1268b3;
  --hero-ink:#14285e;
  --nav:#1c1c1c;
  --accent:#e0452b;
  --go:#1f8a1f;
  --news-link:#1463c9;
  --badge-red:#c8283a;
  --badge-violet:#8a2a6e;
  --footer:#2b2b2b;
  --footer-base:#1a1a1a;
  --footer-text:#8d8d8d;
}
*{box-sizing:border-box;margin:0;padding:0}
html,body{width:1027px;height:1200px;overflow:hidden}
body{
  font-family:"Arimo",Arial,sans-serif;color:var(--body);
  background:linear-gradient(90deg,var(--sky-edge) 0,var(--sky-mid) 150px,var(--sky-mid) 877px,var(--sky-edge) 1027px);
  position:relative;
}
.page{position:absolute;left:176px;top:0;width:677px;height:1076px;background:var(--page);box-shadow:0 0 20px rgba(120,180,220,.35)}
.abs{position:absolute}
.logo{left:229px;top:28px}
.logo-name{font-weight:700;font-size:30px;color:var(--brand);letter-spacing:1px}
.logo-tag{left:229px;top:58px;font-size:7px;font-weight:700;color:var(--brand);letter-spacing:.5px}
.field{height:22px;border:1px solid #cfcfcf;background:#f3f3f3;font-size:10px;color:#a8a8a8;padding:5px 8px}
.login-btn{left:764px;top:31px;width:68px;height:22px;border-radius:4px;background:var(--brand-bright);color:#fff;font-size:11px;text-align:center;line-height:22px}
.nav{left:192px;top:91px;width:642px;height:45px;background:var(--nav);display:flex;align-items:center}
.nav a{color:#fff;text-decoration:none;font-size:12.5px;height:45px;line-height:45px;padding:0 20px}
.nav a.active{background:var(--brand-bright);padding:0 18px}
.search{position:absolute;right:10px;top:13px;width:160px;height:21px;background:#f2f2f2}
.search svg{position:absolute;right:4px;top:3px}
.hero{left:192px;top:136px;width:642px;height:262px;overflow:hidden;
  background:
    linear-gradient(100deg,rgba(0,0,0,0) 0%,rgba(0,0,0,0) 52%,rgba(20,28,44,.45) 68%,rgba(20,28,44,.25) 82%,rgba(0,0,0,0) 100%),
    radial-gradient(ellipse 120px 50px at 130px 215px,rgba(255,255,255,.85),rgba(255,255,255,0)),
    radial-gradient(ellipse 160px 55px at 300px 240px,rgba(255,255,255,.8),rgba(255,255,255,0)),
    radial-gradient(ellipse 110px 40px at 420px 150px,rgba(255,255,255,.55),rgba(255,255,255,0)),
    radial-gradient(ellipse 130px 45px at 590px 205px,rgba(255,255,255,.7),rgba(255,255,255,0)),
    radial-gradient(ellipse 90px 35px at 60px 120px,rgba(255,255,255,.45),rgba(255,255,255,0)),
    linear-gradient(180deg,#14408a 0%,#2b68b6 40%,#5e97d2 72%,#9fc3e6 100%)}
.hero-title{position:absolute;left:61px;background:rgba(42,95,168,.82);font-family:"Montserrat",sans-serif;font-weight:800;color:var(--hero-ink);font-size:22px;letter-spacing:.8px;padding:2px 10px;line-height:32px}
.hero-copy{position:absolute;left:62px;top:109px;width:290px;color:#fff;font-size:10.5px;line-height:13px}
.read-more{position:absolute;left:62px;top:174px;width:68px;height:22px;border-radius:3px;background:var(--go);color:#fff;font-size:10.5px;line-height:22px;text-align:center}
.arrow{position:absolute;top:71px;width:33px;height:39px;background:rgba(255,255,255,.18)}
h2{position:absolute;left:192px;font-size:18.5px;font-weight:700;color:var(--ink)}
.rule{position:absolute;left:192px;width:642px;height:1px;background:var(--rule)}
.intro{left:192px;top:459px;width:642px;font-size:11.7px;line-height:14px}
.intro p{margin-bottom:14px}
.intro ul{list-style:none;margin:0 0 14px}
.intro li::before{content:"›";color:var(--accent);margin-right:10px}
.news-img{left:192px;top:758px;width:179px;height:146px;border:3px solid #333;
  background:
    radial-gradient(circle 26px at 82px 46px,#4f8fd0,#2e6aa8 70%,rgba(46,106,168,0) 100%),
    radial-gradient(ellipse 70px 30px at 88px 108px,rgba(220,240,230,.35),rgba(220,240,230,0)),
    radial-gradient(circle at 50% 45%,#76b192,#3f7c5d 75%,#2f6148 100%)}
.news-title{left:380px;top:766px;color:var(--accent);font-size:12px}
.news-rule{left:380px;top:784px;width:274px;height:1px;background:var(--rule)}
.news-text{left:380px;top:796px;width:274px;font-size:7.6px;line-height:14.5px;color:var(--news-link)}
.news-more{left:382px;top:870px;font-size:8px;color:var(--news-link);text-decoration:underline}
.dots{left:570px;top:894px;display:flex;gap:9px}
.dots i{width:8px;height:8px;border-radius:50%;background:var(--accent)}
.dots i.on{background:#111}
.vline{left:686px;top:757px;width:1px;height:160px;background:var(--rule)}
.partners{left:192px;top:984px;width:642px;height:60px;display:flex;align-items:center;justify-content:space-around}
.partner{font-size:22px;font-weight:700;color:var(--brand);display:flex;align-items:center;gap:6px}
.partner i{display:block;width:14px;height:14px;border-radius:50%;background:var(--brand-bright)}
.footer{left:0;top:1076px;width:1027px;height:104px;background:var(--footer)}
.footer-base{left:0;top:1180px;width:1027px;height:20px;background:var(--footer-base);color:var(--footer-text);font-size:7px;line-height:20px;padding-left:213px}
.flinks{font-size:7px;line-height:11.5px;color:var(--footer-text)}
.fcontact{left:629px;top:1130px;font-size:7px;line-height:9.5px;color:var(--footer-text);display:grid;grid-template-columns:55px 14px auto}
</style>
</head>
<body>
<div class="page"></div>

<header>
  <div class="abs logo"><span class="logo-name">BGL</span></div>
  <div class="abs logo-tag">BRIGHTGRIDLINK</div>
  <div class="abs field" style="left:466px;top:31px;width:138px">Username</div>
  <div class="abs field" style="left:616px;top:31px;width:136px">Password</div>
  <div class="abs login-btn">Login</div>
</header>

<nav class="abs nav">
  <a class="active">Home</a><a>Solutions</a><a>Products</a><a>Case Studies</a><a>Contact Us</a>
  <div class="search"><svg width="15" height="15" viewBox="0 0 15 15"><circle cx="6" cy="6" r="4.5" fill="none" stroke="#333" stroke-width="2"/><line x1="9.5" y1="9.5" x2="14" y2="14" stroke="#333" stroke-width="2.2"/></svg></div>
</nav>

<section class="abs hero" role="img" aria-label="Photo of an electricity pylon and power lines against a blue sky with clouds">
  <div class="hero-title" style="top:31px">PROVIDING</div>
  <div class="hero-title" style="top:63px;padding-right:72px">COMPLETE SOLUTIONS .....</div>
  <p class="hero-copy">Riusto odio dignissimos ducimus qui blanditiis praesentium voluptatum deleniti atque corrupti quos dolores et quas molestias excepturi sint occaecati cupiditate non provident, similique sunt in culpa qui officia deserunt mollitia animi, id est laborum et dolorum fuga.</p>
  <div class="read-more">Read More</div>
  <div class="arrow" style="left:4px"><svg width="33" height="39"><polyline points="20,12 13,19.5 20,27" fill="none" stroke="#fff" stroke-width="2"/></svg></div>
  <div class="arrow" style="right:4px"><svg width="33" height="39"><polyline points="13,12 20,19.5 13,27" fill="none" stroke="#fff" stroke-width="2"/></svg></div>
</section>

<h2 style="top:425px">Welcome to Bright Grid Link</h2>
<div class="rule" style="top:449px"></div>
<div class="abs intro">
  <p>Bright Grid Link provides a web based application to gather data from Electricity Meters, Gas Meters, Water Meters, and other sources via GPRS or Ethernet modems storing the data on Web Servers and providing means by which customers can access their data via a web browser.</p>
  <p>We provide our own custom designed modems to collect the data, these modems automatically connect to the Web Server using GPRS or Ethernet, transmitting the data which is then stored on the server. The modems can handle meters with</p>
  <ul>
    <li>Volt free pulse outputs</li>
    <li>IEC 62056 RS485 serial outputs</li>
    <li>Modbus RS485 serial outputs</li>
    <li>0-5V Analog signals from Temperature, Wind Speed and Solar radiation sensors.</li>
  </ul>
  <p>and also provide two digital outputs that can be used to drive PLC's or relays.</p>
  <p>Our Web servers provide constantly updated meter readings (from 1 minute to hourly readings) which can be viewed using a graphical interface to see the changes over a period of time. The data can be exported in spreadsheet format for futher processing, these spreadsheet files can be emailed directly to a recipient at preset times (weekly, monthly etc.).</p>
</div>

<h2 style="top:714px">Latest News</h2>
<div class="rule" style="top:740px"></div>
<div class="abs news-img" role="img" aria-label="Illustration of a globe connected to computers and devices on a green chalkboard"></div>
<div class="abs news-title">Web based application</div>
<div class="abs news-rule"></div>
<p class="abs news-text">Bright Grid Link provides a web based application to gather data from Electricity Meters, Gas Meters, Water Meters, and other sources via GPRS or Ethernet modems storing the data on Web Servers and providing means by which customers can access their data via a web browser.</p>
<div class="abs news-more">More &nbsp;›</div>
<div class="abs dots"><i></i><i class="on"></i><i></i><i></i><i></i></div>
<div class="abs vline"></div>
<svg class="abs" style="left:722px;top:760px" width="60" height="126" role="img" aria-label="Accreditation badges">
  <circle cx="30" cy="26" r="20" fill="var(--badge-red)"/>
  <rect x="12" y="72" width="36" height="36" fill="var(--badge-violet)"/>
</svg>

<h2 style="top:934px">Our Partners</h2>
<div class="rule" style="top:959px"></div>
<div class="abs partners">
  <span class="partner">Norvex</span>
  <span class="partner"><i></i>Calto</span>
  <span class="partner" style="font-size:17px">Trackline Ways</span>
  <span class="partner">Quenta</span>
  <span class="partner">Lumo Tel</span>
</div>

<footer>
  <div class="abs footer"></div>
  <div class="abs flinks" style="left:213px;top:1089px">About Us<br>Management &amp; Board<br>Why Bright Grid Link?<br>Certifications &amp; Awards<br>Advisory Board<br>Our Offices<br>Contact Us</div>
  <div class="abs flinks" style="left:333px;top:1089px;line-height:9px">Solutions<br>Products<br>Case Studies<br>Demo Request<br>FAQ</div>
  <div class="abs" style="left:629px;top:1092px;font-weight:700;font-size:21px;color:#fff">BGL</div>
  <div class="abs" style="left:629px;top:1114px;font-weight:700;font-size:5px;color:#fff">BRIGHTGRIDLINK</div>
  <div class="abs fcontact">
    <span>Address</span><span>:</span><span>No:18/4, Harlow Quay, NY</span>
    <span>Tel</span><span>:</span><span>+44 100 555 0182</span>
    <span>Fax</span><span>:</span><span>+44 100 555 0947</span>
    <span>Email</span><span>:</span><span>info@bgl-mail.com</span>
  </div>
  <div class="abs footer-base">© 2013 Bright Grid Link. All Rights Reserved.</div>
</footer>
</body>
</html>
```